Stylish Design With Simple UI For Appointment Site

ONE WEEK TO GO - STILL CONSIDERING NEW DESIGNS!

Note: Logo file now attached. Extra credit to anyone who offers basic HTML templates in the final deliverable, incorporating the individual components of the design (using DIVs and CSS).

There are two key requirements for this site:

1. It makes our site look like one of the most professional of its kind. We want to look the part;
2. It has a very simple, straight-forward user interface. We're nothing without being intuitive.

Our site will be used by other businesses to set up their own online booking systems.

Logo samples attached. The colour scheme is not yet set but two possible options are:

1. Dark (#323B3A) & Blue (#12B5D4) on White background
2. White & Yellow (#FEF102) on Grey (#3A3A3C) background

For inspiration, and an idea of what we like, take a look at quillpost.example - it's very clear and eye-catching, although its pages are longer than we would like ours to be. Oh but we don't need a chimp! Instead of the section with the chimp in, we would like a changing image headline section on the home page, in the style of bellvarine.example.co.uk (with a less high image; we have attached one image which you may want to try out with this, but happy to see other ideas).

Any graphics included must be royalty free and free for commercial use. Fonts should be readily available and specified.

We would like to see the design applied to the following pages:

1. The main public home page (features header, login prompt, menu, changing image banner with headlines, main body, footer menu).
2. A secondary public page (features a similar layout to home page but without image headline banner, includes extra panels/body detail).
3. The Control Panel page (features several list panels and an add appointment button).
4. A list-style administration page (with popup item editor window).
5. A settings administration page (with form).

In that order, a sample walk-through design spec will be attached.

To summarise, we are looking for someone to put forward not only a design but something which also focuses on the user interface. The designer should consider all of the examples and guidance given, but shouldn't let that limit any innovation.

Happy to respond to any questions and give constant feedback.

Thank you.

-*-*-*-*-*-*-*-*-*-*-*-*-*-*-*-*-

Update, 18th Nov 2011:

1. I'm about the upload the logos so you can incorporate these into your designs.

2. A UI question of mine is how to move from a list view (e.g. Resources) to editing one of those items in the list. In the spec document I showed a popup editor for these items but I don't know if that's the best thing to do. Happy to see other ideas on this - whatever the best user experience would be.

3. On the designs in the spec document I've not included any help functionality. It would be good to include pieces of guidance on each page of the administration area to help the user - guess these could either be info panels on the pages themselves or info popups. Again, would be good to see some ideas in the designs.

Also, just to be clear, I am really looking for something that looks like a modern innovative "web app" rather than it looking like a promotional corporate web site.

Target Market(s)

Owners of businesses of all types (e.g. salons, small hotels, surgeries, etc).

Industry/Entity Type

Commercial

Requirements
Must have
• Headline image transition panel on home page.

Layout, graphic and font styles along similar lines to quillpost.example, bellvarine.example.co.uk, etc.
Nice to have
• Blog feed panel on the home page.

Innovative ideas for improvements to the spec.
Should not have
• Anything which can't be practically rendered when the design is converted to HTML.

Should not be overly influenced by the layout and style in the attached spec - that should just be a guide to the content and layout of the site.

```html
<!DOCTYPE html>
<html lang="en">
<head>
<meta charset="utf-8">
<title>Slotwise – Online Booking</title>
<link href="https://fonts.googleapis.com/css2?family=Arimo:wght@400;700&display=swap" rel="stylesheet">
<style>
  :root {
    --charcoal: #3a3a3c;
    --yellow-top: #fff200;
    --yellow-bottom: #fdc300;
    --ink: #111111;
    --text-grey: #6e6e6e;
    --heading-grey: #333333;
    --page-bg: #f6f7f7;
    --panel-line: #c9c9c9;
    --white: #ffffff;
  }
  * { box-sizing: border-box; margin: 0; padding: 0; }
  html, body { width: 1200px; height: 1161px; overflow: hidden; }
  body {
    position: relative;
    font-family: "Arimo", Arial, sans-serif;
    background: var(--page-bg);
    color: var(--heading-grey);
  }
  .site-header {
    position: absolute; left: 0; top: 14px; width: 1200px; height: 236px;
    background: var(--charcoal);
  }
  .brand {
    position: absolute; left: 112px; top: 112px;
    display: flex; align-items: center; gap: 14px;
    color: var(--white); font-size: 30px; font-weight: 400; letter-spacing: 5px;
  }
  .brand-mark { width: 26px; height: 26px; background: var(--yellow-top); }
  .main-nav {
    position: absolute; left: 110px; top: 210px;
    display: flex; gap: 44px; list-style: none;
  }
  .main-nav li { color: var(--white); font-size: 24px; font-weight: 700; }
  .main-nav li:nth-child(3) { margin-left: -4px; }
  .login-panel {
    position: absolute; left: 762px; top: 0; width: 331px; height: 175px;
    background: linear-gradient(var(--yellow-top), var(--yellow-bottom));
    border-radius: 0 0 8px 8px;
    box-shadow: 0 2px 4px rgba(0,0,0,.35);
  }
  .locale { position: absolute; right: 52px; top: 9px; font-size: 12px; color: var(--ink); }
  .account-links { position: absolute; left: 44px; top: 29px; font-size: 14px; color: var(--ink); }
  .account-links span { text-decoration: underline; }
  .field {
    position: absolute; left: 41px; width: 238px; height: 32px;
    background: var(--white); border: 1px solid #d9b800; border-radius: 3px;
    padding: 7px 9px; font-size: 16px; color: #9a9a9a;
  }
  .field-user { top: 55px; }
  .field-pass { top: 100px; }
  .login-small {
    position: absolute; left: 185px; top: 139px; width: 90px; height: 31px;
    background: #2a2a2a; color: var(--white); border-radius: 4px;
    font-size: 17px; font-weight: 700; text-align: center; line-height: 31px;
  }
  .hero {
    position: absolute; left: 97px; top: 250px; width: 1006px; height: 535px;
    border-radius: 0 0 6px 6px; overflow: hidden;
    box-shadow: 0 4px 6px rgba(0,0,0,.3);
  }
  .hero-photo {
    position: absolute; inset: 0;
    background: radial-gradient(ellipse at 30% 45%, #f2f2f2 0%, #d6d6d6 35%, #9a9a9a 60%, #2a2a2a 78%, #050505 90%);
  }
  .hero-headline {
    position: absolute; left: 86px; top: 91px; width: 787px; height: 61px;
    background: rgba(235,235,235,.72);
    font-size: 42px; font-weight: 700; color: var(--ink);
    text-align: right; padding: 6px 4px 0 0;
  }
  .hero-text {
    position: absolute; left: 346px; top: 159px; width: 527px; height: 121px;
    background: rgba(235,235,235,.72);
    font-size: 23px; line-height: 28.5px; color: var(--ink);
    text-align: right; padding: 5px 9px 0 0;
  }
  .cta {
    position: absolute; background: linear-gradient(var(--yellow-top), var(--yellow-bottom));
    color: var(--heading-grey); font-weight: 700; text-align: center; border-radius: 5px;
  }
  .hero-cta { left: 693px; top: 310px; width: 169px; height: 56px; font-size: 36px; line-height: 52px; }
  .slider-arrow {
    position: absolute; top: 451px; width: 109px; height: 89px;
    background: linear-gradient(var(--yellow-top), var(--yellow-bottom));
    border-radius: 5px; display: flex; align-items: center; justify-content: center;
  }
  .arrow-prev { left: 90px; }
  .arrow-next { left: 1000px; }
  .slider-dots { position: absolute; left: 402px; top: 499px; display: flex; gap: 10px; }
  .slider-dots span {
    width: 23px; height: 23px; border-radius: 50%;
    background: #d4d4d4; border: 2px solid #a0a0a0;
  }
  .slider-dots .is-active { background: var(--yellow-top); border-color: #c9a600; }
  .info-panel {
    position: absolute; top: 815px; height: 265px;
    background: linear-gradient(var(--white), #f1f1f1);
    border: 1px solid var(--panel-line); border-radius: 6px;
  }
  .panel-news { left: 100px; width: 486px; }
  .panel-available { left: 614px; width: 489px; }
  .panel-title { position: absolute; font-size: 23px; font-weight: 700; color: var(--heading-grey); }
  .panel-news .panel-title { left: 230px; top: 23px; }
  .panel-available .panel-title { left: 36px; top: 22px; }
  .news-date {
    position: absolute; left: 84px; top: 83px; width: 356px;
    font-size: 16px; font-weight: 700; color: var(--ink);
    border-bottom: 1px solid #555; padding-bottom: 1px;
  }
  .panel-copy { position: absolute; font-size: 16px; line-height: 20px; color: var(--text-grey); }
  .panel-news .panel-copy { left: 83px; top: 112px; width: 345px; }
  .panel-available .panel-copy { left: 37px; top: 82px; width: 430px; }
  .panel-more { top: 206px; width: 118px; height: 40px; font-size: 22px; line-height: 40px; }
  .panel-news .panel-more { left: 322px; }
  .panel-available .panel-more { left: 327px; }
  .news-ribbon { position: absolute; left: 93px; top: 810px; }
  .site-footer {
    position: absolute; left: 101px; top: 1121px; width: 1001px;
    display: flex; justify-content: space-between;
    font-size: 17px; color: #555;
  }
  .frame { position: absolute; inset: 0; border: 1px solid #bdbdbd; pointer-events: none; }
</style>
</head>
<body>
  <header class="site-header">
    <div class="brand"><span class="brand-mark"></span>Slotwise</div>
    <ul class="main-nav">
      <li>HOME</li><li>FEATURES</li><li>PRICING</li><li>CONTACT US</li>
    </ul>
  </header>

  <aside class="login-panel">
    <div class="locale">U.S. I EN</div>
    <div class="account-links"><span>Forgotten Password?</span> I <span>Register</span></div>
    <div class="field field-user">Username</div>
    <div class="field field-pass">Password</div>
    <div class="login-small">Login</div>
  </aside>

  <section class="hero">
    <div class="hero-photo" role="img" aria-label="Close-up photograph of a clock face with black hands and numeral"></div>
    <h1 class="hero-headline">There are many variations of passages</h1>
    <p class="hero-text">of Lorem Ipsum available, but the majority have suffered alteration in some form, by injected humour, or randomised words which don't look even slightly believable.</p>
    <div class="cta hero-cta">Login</div>
    <div class="slider-dots"><span></span><span class="is-active"></span><span></span><span></span><span></span></div>
  </section>

  <div class="slider-arrow arrow-prev">
    <svg width="44" height="44" viewBox="0 0 44 44"><path d="M30 4 L12 22 L30 40" fill="none" stroke="#fff" stroke-width="9"/></svg>
  </div>
  <div class="slider-arrow arrow-next">
    <svg width="44" height="44" viewBox="0 0 44 44"><path d="M14 4 L32 22 L14 40" fill="none" stroke="#fff" stroke-width="9"/></svg>
  </div>

  <section class="info-panel panel-news">
    <h2 class="panel-title">What’s Happening?</h2>
    <div class="news-date">3 October 2011</div>
    <p class="panel-copy">The Internet tend to repeat predefined chunks as necessary, making this the first true generator on the Internet. It uses a dictionary of over 200 Latin words, combined with a handful</p>
    <div class="cta panel-more">More</div>
  </section>

  <svg class="news-ribbon" width="136" height="132" viewBox="0 0 136 132">
    <defs>
      <linearGradient id="ribbonFill" x1="0" y1="0" x2="1" y2="1">
        <stop offset="0" stop-color="#fff200"/><stop offset="1" stop-color="#fdc300"/>
      </linearGradient>
    </defs>
    <path d="M0 0 H135 L0 131 Z" fill="url(#ribbonFill)"/>
    <text x="42" y="60" transform="rotate(-45 42 60)" text-anchor="middle" font-family="Arimo, Arial, sans-serif" font-size="19" font-weight="700" fill="#111">NEWS</text>
  </svg>

  <section class="info-panel panel-available">
    <h2 class="panel-title">Make Yourself Available</h2>
    <p class="panel-copy">Of Lorem Ipsum available, but the majority have suffered alteration in some form, by injected humour, or randomised words which don't look even slightly believable. If you are going to use a passage of Lorem Ipsum</p>
    <div class="cta panel-more">More</div>
  </section>

  <footer class="site-footer">
    <span>Copyright © 2011 Slotwise. All Rights Reserved</span>
    <span>HOME &nbsp;|&nbsp; FEATURES &nbsp;|&nbsp; PRICING &nbsp;|&nbsp; CONTACT US</span>
  </footer>

  <div class="frame"></div>
</body>
</html>
```